Lantern Cove Summer Camps Banner Ads

Seeking to create 6 banner ads (two variations of 3 banner sizes. 1) 250x250 2)468x60 3)120x600.
We are a Spanish and French immersion summer camp based in Chapel Hill, North Carolina. You can view our website at http://lanterncove-example.org
We've included our logo attached, colors should be reflective of branded colors in the logo.
Our target market is the South East, United State (FL, GA, NC, SC, TN, VA). Parents (focus on mothers) with kids from grades 1-12 (ages 5-17).
Our calls to action are to register/sign up for camps, and explore our website (Goal is clicks not views).
Language for ad: English.
Final design should be a fun, family-centric ad, which encapsulates the user and encourages them to learn more about Lantern Cove. Preferably, ad can be used ever-green for reuse in different seasons (does not contain date restrictions, for example ad should NOT contain "Join us for Summer Camp 2018").
Typical tag lines include: Friends, languages and a lot of fun! All the fun of a summer camp while totally immersed in the language and culture!
Target Market(s)

```html
<!DOCTYPE html>
<html lang="en">
<head>
<meta charset="utf-8">
<title>Lantern Cove Summer Camps Banner Ads</title>
<link href="https://fonts.googleapis.com/css2?family=Oswald:wght@400;500&family=Gochi+Hand&family=Crimson+Text&display=swap" rel="stylesheet">
<style>
  :root {
    --page: #e4e6e9;
    --white: #ffffff;
    --sky: #2f9dd8;
    --sky-deep: #2386c2;
    --teal: #17a38c;
    --teal-deep: #0e8672;
    --brand: #2a8fd0;
    --dot: #3aa34a;
    --mint-top: #f2fbf6;
    --mint-bottom: #bfe6d4;
    --mint-text: #2f6b3c;
    --go-top: #6fd04a;
    --go-bottom: #2e9b22;
    --photo-a: #6f9fc9;
    --photo-b: #9cb878;
    --grass-a: #8fb4c9;
    --grass-b: #5f9a3e;
    --shadow: rgba(0,0,0,.18);
  }
  * { box-sizing: border-box; margin: 0; padding: 0; }
  html, body { width: 1200px; height: 1200px; overflow: hidden; }
  body { background: var(--page); position: relative; font-family: "Crimson Text", serif; }

  .banner { position: absolute; overflow: hidden; background: var(--sky); box-shadow: 0 12px 18px -8px var(--shadow); }
  .banner svg { position: absolute; left: 0; top: 0; }

  .photo { position: absolute; }
  .photo--group { background: linear-gradient(160deg, var(--photo-a), #8fb1d3 45%, var(--photo-b)); }
  .photo--field { background: linear-gradient(180deg, var(--grass-a) 0%, #b9cfd8 30%, var(--grass-b) 55%, #4d8a33 100%); }

  .brand { position: absolute; display: flex; align-items: center; justify-content: center; gap: 6px;
           font-family: "Oswald", sans-serif; font-weight: 500; color: var(--brand); white-space: nowrap; }
  .brand__dot { width: 10px; height: 10px; border-radius: 50%; background: var(--dot); }

  .headline { position: absolute; font-family: "Oswald", sans-serif; font-weight: 500; color: var(--white);
              text-transform: uppercase; line-height: 1.1; }
  .headline small { display: block; font-size: .78em; font-weight: 400; }
  .script { position: absolute; font-family: "Gochi Hand", cursive; color: var(--white); line-height: 1.25; text-align: center; }
  .body-copy { position: absolute; font-family: "Crimson Text", serif; color: #f4f9fd; line-height: 1.3; text-align: center; }

  .btn { position: absolute; display: flex; align-items: center; justify-content: center;
         font-family: "Oswald", sans-serif; text-transform: uppercase; border-radius: 6px; }
  .btn--register { background: linear-gradient(var(--mint-top), var(--mint-bottom)); color: var(--mint-text);
                   border: 1px solid #9fd3bb; font-weight: 400; }
  .btn--signup { background: linear-gradient(var(--go-top), var(--go-bottom)); color: var(--white);
                 border: 1px solid #2a8a1f; font-weight: 500; border-radius: 3px; }
</style>
</head>
<body>

<!-- Skyscraper A -->
<div class="banner sky-a" style="left:188px;top:56px;width:164px;height:826px;background:var(--white)">
  <div class="brand" style="left:0;top:78px;width:164px;font-size:18px"><span class="brand__dot"></span>Lantern Cove</div>
  <div class="photo photo--field" role="img" aria-label="Children running across a sports field in a ladder drill" style="left:0;top:240px;width:164px;height:240px"></div>
  <svg width="164" height="826" viewBox="0 0 164 826" aria-hidden="true">
    <path d="M0,370 C40,450 110,500 164,505 V826 H0 Z" fill="var(--teal)"/>
    <path d="M0,395 C40,470 110,520 164,530 V826 H0 Z" fill="var(--sky)"/>
  </svg>
  <div class="headline" style="left:0;top:566px;width:164px;text-align:center;font-size:15px">
    Friends, languages<br>and a lot of fun!
    <small style="font-size:11.5px;margin-top:2px">All the fun of a summer camp<br>while totally immersed<br>in the language and culture!</small>
  </div>
  <div class="btn btn--register" style="left:8px;top:740px;width:148px;height:40px;font-size:17px">Register</div>
</div>

<!-- Skyscraper B -->
<div class="banner sky-b" style="left:384px;top:56px;width:164px;height:826px;background:var(--white)">
  <div class="photo photo--group" role="img" aria-label="Group of smiling campers in blue camp shirts posing together" style="left:0;top:0;width:164px;height:288px"></div>
  <div class="brand" style="left:0;top:312px;width:164px;font-size:18px"><span class="brand__dot"></span>Lantern Cove</div>
  <svg width="164" height="826" viewBox="0 0 164 826" aria-hidden="true">
    <path d="M0,372 H140 Q164,372 164,396 V826 H0 Z" fill="var(--sky)"/>
  </svg>
  <div class="script" style="left:0;top:442px;width:164px;font-size:22px">Friends,<br>languages and<br>a lot of fun!</div>
  <div class="body-copy" style="left:10px;top:560px;width:144px;font-size:14px">All the fun of a summer camp while totally immersed in the language and culture!</div>
  <div class="btn btn--signup" style="left:6px;top:708px;width:152px;height:42px;font-size:17px">Sign up for camps</div>
</div>

<!-- Square A -->
<div class="banner square-a" style="left:599px;top:54px;width:403px;height:403px;background:var(--white)">
  <div class="photo photo--field" role="img" aria-label="Children running across a sports field in a ladder drill" style="left:60px;top:90px;width:343px;height:250px"></div>
  <svg width="403" height="403" viewBox="0 0 403 403" aria-hidden="true">
    <path d="M0,0 H403 V90 H150 Q80,95 40,60 L0,40 Z" fill="var(--white)"/>
    <path d="M0,40 Q50,70 70,120 C30,230 0,300 0,403 Z" fill="var(--white)"/>
    <path d="M0,40 C60,70 70,140 80,190 C110,280 230,310 403,290 V335 C220,345 70,320 0,230 Z" fill="var(--teal)"/>
    <path d="M0,262 C80,330 220,355 403,330 V403 H0 Z" fill="var(--sky)"/>
  </svg>
  <div class="brand" style="left:50px;top:30px;width:180px;font-size:20px"><span class="brand__dot"></span>Lantern Cove</div>
  <div class="headline" style="left:11px;top:292px;font-size:18px">
    Friends, languages<br>and a lot of fun!
    <small style="font-size:12px;margin-top:3px">All the fun of a summer camp<br>while totally immersed<br>in the language and culture!</small>
  </div>
  <div class="btn btn--register" style="left:211px;top:348px;width:172px;height:44px;font-size:19px">Register</div>
</div>

<!-- Square B -->
<div class="banner square-b" style="left:599px;top:479px;width:403px;height:403px">
  <div class="photo photo--group" role="img" aria-label="Group of smiling campers in blue camp shirts posing together" style="left:0;top:0;width:186px;height:403px"></div>
  <svg width="403" height="403" viewBox="0 0 403 403" aria-hidden="true">
    <path d="M204,0 H403 V90 H224 Q204,90 204,70 Z" fill="var(--white)"/>
  </svg>
  <div class="brand" style="left:204px;top:30px;width:199px;font-size:20px"><span class="brand__dot"></span>Lantern Cove</div>
  <div class="script" style="left:186px;top:134px;width:217px;font-size:23px">Friends, languages<br>and a lot of fun!</div>
  <div class="body-copy" style="left:196px;top:236px;width:197px;font-size:16px">All the fun of a summer camp while totally immersed in the language and culture!</div>
  <div class="btn btn--signup" style="left:202px;top:340px;width:184px;height:46px;font-size:20px">Sign up for camps</div>
</div>

<!-- Leaderboard A -->
<div class="banner board-a" style="left:172px;top:912px;width:872px;height:110px">
  <div class="photo photo--group" role="img" aria-label="Group of smiling campers in blue camp shirts posing together" style="left:0;top:0;width:240px;height:110px"></div>
  <svg width="872" height="110" viewBox="0 0 872 110" aria-hidden="true">
    <path d="M690,0 H872 V66 H712 Q690,66 690,44 Z" fill="var(--white)"/>
  </svg>
  <div class="brand" style="left:690px;top:18px;width:182px;font-size:17px"><span class="brand__dot"></span>Lantern Cove</div>
  <div class="script" style="left:262px;top:8px;width:380px;text-align:left;font-size:22px">Friends, languages and a lot of fun!</div>
  <div class="body-copy" style="left:262px;top:44px;width:400px;text-align:left;font-size:15px;line-height:1.25">All the fun of a summer camp while totally immersed<br>in the language and culture!</div>
  <div class="btn btn--signup" style="left:476px;top:70px;width:172px;height:36px;font-size:17px">Sign up for camps</div>
</div>

<!-- Leaderboard B -->
<div class="banner board-b" style="left:172px;top:1050px;width:875px;height:110px">
  <div class="photo photo--field" role="img" aria-label="Children running across a sports field in a ladder drill" style="left:0;top:0;width:560px;height:110px"></div>
  <svg width="875" height="110" viewBox="0 0 875 110" aria-hidden="true">
    <path d="M0,0 H190 Q150,30 110,48 Q60,62 0,60 Z" fill="var(--white)"/>
    <path d="M500,0 C540,40 560,80 580,110 H875 V0 Z" fill="var(--teal)"/>
    <path d="M530,0 C570,40 590,80 610,110 H875 V0 Z" fill="var(--sky)"/>
  </svg>
  <div class="brand" style="left:0;top:10px;width:150px;font-size:15px"><span class="brand__dot"></span>Lantern Cove</div>
  <div class="headline" style="left:466px;top:24px;width:190px;text-align:right;font-size:22px">Friends, languages<br>and a lot of fun!</div>
  <div class="btn btn--register" style="left:674px;top:30px;width:184px;height:52px;font-size:22px">Register</div>
</div>

</body>
</html>
```